Redesign Business Cards, Attached

Please read instructions carefully. If you have any questions send a message before submitting your ONE design. Please redesign attached business cards. Double sided. Use same content and descriptions. Use black, silver, crimson red and gold colors. My only issue with the attached design is the background colors. I like the layout as-is. I can provide the individual pictures on the back side later. Do not submit more than one design. One submission shall include both front and back. Do not submit front and back separately. A second project will be launched to create a matching post card after completion of this.
Industry/Entity Type
see description and attachments.
Contact Information for Business Card
Requirements
Must have
- see description and attachments.
Nice to have
Should not have

```html
<!DOCTYPE html>
<html lang="en">
<head>
<meta charset="UTF-8">
<title>Harbor Crest Boat Training &amp; Charters – Business Card</title>
<link rel="stylesheet" href="https://fonts.googleapis.com/css2?family=Montserrat:wght@400;500;700;800&display=swap">
<style>
  :root {
    --stage: #2a2b2e;
    --black: #0d0d0f;
    --charcoal: #1c1c20;
    --graphite: #2e2f34;
    --crimson: #a3141f;
    --crimson-deep: #5e0a12;
    --gold: #d4a72c;
    --silver: #c9ccd1;
    --silver-light: #e6e8eb;
  }
  * { box-sizing: border-box; margin: 0; padding: 0; }
  html, body {
    width: 1200px; height: 900px; overflow: hidden;
    background: var(--stage);
    font-family: "Montserrat", sans-serif;
  }
  .stage {
    position: relative; width: 1200px; height: 900px;
    display: flex; align-items: center; justify-content: center; gap: 40px;
  }
  .card {
    position: relative; width: 540px; height: 309px;
    overflow: hidden; border-radius: 3px;
    box-shadow: 0 18px 40px rgba(0,0,0,0.55);
  }

  /* Front */
  .card--front {
    background: linear-gradient(160deg, var(--graphite) 0%, var(--black) 100%);
  }
  .front__band {
    position: absolute; left: 0; top: 0; bottom: 0; width: 22px;
    background: var(--gold);
  }
  .front__band::after {
    content: ""; position: absolute; right: -4px; top: 0; bottom: 0; width: 4px;
    background: var(--crimson);
  }
  .brand {
    position: absolute; display: flex; flex-direction: column; align-items: center; gap: 10px;
    text-align: center;
  }
  .brand__dot {
    width: 66px; height: 66px; border-radius: 50%;
    background: var(--silver-light); border: 3px solid var(--gold);
  }
  .brand__name {
    color: var(--silver-light); font-weight: 700; font-size: 13px; line-height: 1.35;
    letter-spacing: 0.5px; text-transform: uppercase;
  }
  .card--front .brand { left: 48px; top: 80px; width: 180px; }
  .front__divider {
    position: absolute; left: 250px; top: 70px; width: 1px; height: 170px;
    background: var(--gold); opacity: 0.8;
  }
  .identity { position: absolute; left: 272px; top: 76px; right: 20px; }
  .identity__name {
    color: var(--gold); font-weight: 800; font-size: 22px; letter-spacing: 0.4px;
    text-transform: uppercase; white-space: nowrap;
  }
  .identity__role {
    color: var(--silver-light); font-weight: 500; font-size: 14px; line-height: 1.35; margin-top: 4px;
  }
  .contact { list-style: none; margin-top: 16px; }
  .contact__item {
    display: flex; align-items: center; gap: 8px;
    color: var(--silver); font-weight: 500; font-size: 13.5px; line-height: 1.7;
    white-space: nowrap;
  }
  .contact__icon { width: 11px; height: 11px; flex: none; }

  /* Back */
  .card--back { background: var(--black); }
  .back__photo {
    position: absolute; inset: 0;
    background: radial-gradient(ellipse at 62% 55%, var(--graphite) 0%, var(--charcoal) 45%, var(--black) 100%);
  }
  .back__photo::after {
    content: ""; position: absolute; left: 0; right: 0; bottom: 0; height: 5px;
    background: var(--crimson);
  }
  .card--back .brand { left: 250px; top: 26px; width: 170px; }
  .badges { position: absolute; right: 22px; top: 66px; display: flex; gap: 10px; }
  .badge { width: 40px; height: 40px; border-radius: 50%; border: 2px solid var(--silver); }
  .badge--silver { background: var(--graphite); }
  .badge--crimson { background: var(--crimson); }
  .services {
    position: absolute; left: 24px; right: 20px; bottom: 36px; list-style: none;
  }
  .services__line {
    color: var(--silver-light); font-weight: 500; font-size: 12.5px; line-height: 1.75;
    white-space: nowrap;
  }
  .services__sep { color: var(--gold); font-weight: 700; margin: 0 4px; }
</style>
</head>
<body>
<main class="stage">

  <section class="card card--front" aria-label="Business card front">
    <div class="front__band"></div>
    <div class="brand">
      <span class="brand__dot"></span>
      <span class="brand__name">Harbor Crest Boat Training &amp; Charters</span>
    </div>
    <div class="front__divider"></div>
    <div class="identity">
      <h1 class="identity__name">Dana R. Whitlow</h1>
      <p class="identity__role">USCG Licensed Captain<br>Certified Instructor</p>
      <ul class="contact">
        <li class="contact__item">
          <svg class="contact__icon" viewBox="0 0 12 12"><path fill="#d4a72c" d="M2.5 0.5l2 2.4-1 1.3a7 7 0 0 0 4.3 4.3l1.3-1 2.4 2-1.2 1.8C5.6 11 1 6.4 0.7 1.7z"/></svg>
          (555) 014-2290
        </li>
        <li class="contact__item">
          <svg class="contact__icon" viewBox="0 0 12 12"><rect x="0.5" y="2" width="11" height="8" rx="1" fill="#d4a72c"/><path d="M1 2.5l5 4 5-4" stroke="#1c1c20" stroke-width="1.2" fill="none"/></svg>
          hello@harborcrestboats.com
        </li>
        <li class="contact__item">
          <svg class="contact__icon" viewBox="0 0 12 12"><circle cx="6" cy="6" r="5.5" fill="#d4a72c"/><path d="M0.5 6h11M6 0.5c-2.5 3-2.5 8 0 11M6 0.5c2.5 3 2.5 8 0 11" stroke="#1c1c20" stroke-width="0.9" fill="none"/></svg>
          www.HarborCrestBoats.com
        </li>
      </ul>
    </div>
  </section>

  <section class="card card--back" aria-label="Business card back">
    <div class="back__photo" role="img" aria-label="Aerial photograph of a motor boat cruising across open water"></div>
    <div class="brand">
      <span class="brand__dot"></span>
      <span class="brand__name">Harbor Crest Boat Training &amp; Charters</span>
    </div>
    <div class="badges">
      <span class="badge badge--silver" role="img" aria-label="Instructor certification badge"></span>
      <span class="badge badge--crimson" role="img" aria-label="Membership badge"></span>
    </div>
    <ul class="services">
      <li class="services__line">Hands-On Boat Training<span class="services__sep">|</span>Introduction to Power boating<span class="services__sep">|</span>Coastal Navigation</li>
      <li class="services__line">Open Water Boat Handling<span class="services__sep">|</span>Captaining / Piloting Service for Your Outings</li>
      <li class="services__line">Precision Docking &amp; Boat Handling<span class="services__sep">|</span>Open Water Advanced Maneuvers</li>
    </ul>
  </section>

</main>
</body>
</html>
```